Business Card Design Project - Photographer

Photography business needs a logo. I would like to see creative licence on options on 1 & 2 sided. I really like the concept of a fully / partially frosted design. I have already used ArtHive for my Logo, so I am looking for the same level of assistance with this project.

If you have any questions please let me know

Cheers Dorian

Reason: Unsure why but the duration was not even a day long

Industry/Entity Type

Business

Requirements
Must have
• These are my contact details
Name: Dorian Welcombe
Mobile: 0438 612 907
email: dorian@brightlensstudio.com.au
Website: www.brightlensstudio.com.au
Nice to have
• Facebook: https://www.facebook.com/BrightLensStudioOz

```html
<!DOCTYPE html>
<html lang="en">
<head>
<meta charset="utf-8">
<title>Bright Lens Studio – Business Card</title>
<link rel="stylesheet" href="https://fonts.googleapis.com/css2?family=Open+Sans:wght@400;600;700&display=swap">
<style>
  :root {
    --page-bg: #ecebe8;
    --frost-light: #d3cbc0;
    --frost-dark: #b9afa2;
    --frost-edge: rgba(255, 255, 255, 0.55);
    --brand-red: #c8212f;
    --ink: #1e1e1e;
    --ink-soft: #3a3a3a;
  }
  * { box-sizing: border-box; margin: 0; padding: 0; }
  html, body {
    width: 1200px;
    height: 800px;
    overflow: hidden;
  }
  body {
    background: var(--page-bg);
    font-family: "Open Sans", Arial, sans-serif;
    display: flex;
    align-items: center;
    justify-content: center;
  }
  .business-card {
    position: relative;
    width: 860px;
    height: 540px;
    border-radius: 26px;
    background: linear-gradient(135deg, var(--frost-light), var(--frost-dark));
    box-shadow: inset 0 0 0 3px var(--frost-edge), 0 10px 30px rgba(0, 0, 0, 0.18);
    color: var(--ink);
  }
  .brand {
    position: absolute;
    left: 60px;
    top: 120px;
  }
  .brand__row {
    display: flex;
    align-items: center;
    gap: 12px;
    white-space: nowrap;
  }
  .brand__mark {
    width: 30px;
    height: 30px;
    background: var(--brand-red);
    flex: none;
  }
  .brand__name {
    font-size: 25px;
    font-weight: 600;
    color: var(--ink-soft);
    line-height: 1.1;
    letter-spacing: 0.5px;
  }
  .brand__tagline {
    margin-top: 8px;
    margin-left: 42px;
    font-size: 16px;
    font-weight: 400;
    color: var(--ink-soft);
    letter-spacing: 0.5px;
    white-space: nowrap;
  }
  .holder-name {
    position: absolute;
    left: 440px;
    top: 112px;
    font-size: 40px;
    font-weight: 700;
    letter-spacing: -0.5px;
    white-space: nowrap;
  }
  .holder-name__first { color: var(--brand-red); }
  .holder-name__last { color: var(--ink); }
  .contact-list {
    position: absolute;
    left: 420px;
    top: 200px;
    list-style: none;
  }
  .contact-list__item {
    display: flex;
    align-items: center;
    gap: 8px;
    height: 42px;
    font-size: 21px;
    font-weight: 600;
    color: var(--ink);
    white-space: nowrap;
  }
  .contact-list__icon {
    width: 22px;
    height: 22px;
    flex: none;
  }
  .contact-list__sep { color: var(--brand-red); margin-right: 4px; }
  .social-link {
    position: absolute;
    left: 380px;
    top: 400px;
    font-size: 21px;
    font-weight: 700;
    color: var(--ink);
    white-space: nowrap;
  }
  .social-link__host { color: var(--brand-red); }
</style>
</head>
<body>
  <main class="business-card">
    <div class="brand">
      <div class="brand__row">
        <span class="brand__mark"></span>
        <span class="brand__name">BRIGHT LENS STUDIO</span>
      </div>
      <p class="brand__tagline">where moments shine</p>
    </div>

    <h1 class="holder-name"><span class="holder-name__first">Dorian</span> <span class="holder-name__last">Welcombe</span></h1>

    <ul class="contact-list">
      <li class="contact-list__item">
        <svg class="contact-list__icon" viewBox="0 0 24 24" aria-hidden="true">
          <path d="M6.5 3.5 9 3l1.8 4.2-2 1.4a11 11 0 0 0 6.6 6.6l1.4-2L21 15l-.5 2.5c-.3 1.4-1.7 2.3-3.1 2A15 15 0 0 1 4 6.6c-.3-1.4.6-2.8 2-3.1Z" fill="var(--brand-red)"/>
        </svg>
        <span class="contact-list__sep">:</span>0438 612 907
      </li>
      <li class="contact-list__item">
        <svg class="contact-list__icon" viewBox="0 0 24 24" aria-hidden="true">
          <rect x="2" y="5" width="20" height="14" rx="1.5" fill="var(--brand-red)"/>
          <path d="M2.5 6 12 13l9.5-7" fill="none" stroke="#f2e6e0" stroke-width="1.6"/>
        </svg>
        <span class="contact-list__sep">:</span>dorian@brightlensstudio.com.au
      </li>
      <li class="contact-list__item">
        <svg class="contact-list__icon" viewBox="0 0 24 24" aria-hidden="true">
          <g fill="none" stroke="var(--brand-red)" stroke-width="1.8">
            <circle cx="12" cy="12" r="9"/>
            <ellipse cx="12" cy="12" rx="4" ry="9"/>
            <path d="M3 12h18M5 7h14M5 17h14"/>
          </g>
        </svg>
        <span class="contact-list__sep">:</span>www.brightlensstudio.com.au
      </li>
    </ul>

    <p class="social-link"><span class="social-link__host">circlepage.com/</span>BrightLensStudioOz</p>
  </main>
</body>
</html>
```